Company Profile for Consulting Comany

Need Company profile to be designed in a professional way.

for inspiring :-
https://www.vimolia.net/gallery/5307462/COMPANY-PROFILE
https://www.vimolia.net/gallery/20934617/Biotech-Product-Catalog-No1-(Laminar-Air-Flow)
https://www.vimolia.net/gallery/38720954/RKT-Tramvale-Company-Profile-2014-(RKT-Rebrand-part-2)

Target Market(s)

Corporate

Industry/Entity Type

It Company

Font styles to use
Sans Serif

Requirements
Must have
• Landscape A4 size
• Must go with the logo branding
• Must Have Visual Identity is the most important
• Must Have mpty spaces

```html
<!DOCTYPE html>
<html lang="en">
<head>
<meta charset="utf-8">
<title>Shift Vector – Company Profile Covers</title>
<link rel="stylesheet" href="https://fonts.googleapis.com/css2?family=Exo+2:wght@300;400;600;700&family=Oswald:wght@600;700&display=swap">
<style>
  :root{
    --cyan:#1fa3d1;
    --ink:#1c1c1e;
    --graphite:#333538;
    --paper:#ffffff;
    --backdrop:#c9c9c9;
    --photo-deep:#1d2a44;
    --photo-mid:#5c7599;
    --photo-light:#d9e3ef;
  }
  *{box-sizing:border-box;margin:0;padding:0}
  html,body{width:1200px;height:1200px;overflow:hidden}
  body{background:var(--backdrop);font-family:"Exo 2",sans-serif;position:relative}
  .cover{position:absolute;left:220px;width:760px;height:537px;background:var(--paper);overflow:hidden;box-shadow:0 10px 28px rgba(0,0,0,.22)}
  .cover--front{top:40px}
  .cover--back{top:623px}
  .layer{position:absolute;left:0;top:0}

  /* front */
  .headline{position:absolute;left:250px;top:30px;line-height:1}
  .headline__lead{font-weight:300;font-size:34px;letter-spacing:1px;color:var(--graphite)}
  .headline__lead .accent{color:var(--cyan)}
  .headline__main{font-family:"Oswald",sans-serif;font-weight:700;font-size:56px;color:var(--graphite);letter-spacing:-.5px;margin-top:4px}
  .headline__main .accent{color:var(--cyan)}
  .front-photo{position:absolute;left:0;top:150px;width:760px;height:260px;
    background:linear-gradient(180deg,rgba(255,255,255,0) 0%,var(--photo-light) 18%,var(--photo-mid) 55%,var(--photo-deep) 100%)}
  .front-phone,.front-web{position:absolute;font-size:14px;font-weight:600;color:var(--paper);display:flex;align-items:center;gap:6px}
  .front-phone{left:28px;top:392px}
  .front-web{right:36px;top:458px}

  .brand{position:absolute;display:flex;align-items:center;gap:8px;color:var(--cyan);font-weight:600}
  .brand__dot{width:12px;height:12px;border-radius:50%;background:var(--cyan)}
  .brand__name{font-size:26px;line-height:1}
  .brand__tag{font-size:10px;font-weight:400;letter-spacing:2px;color:#bfc3c7;margin-top:3px}
  .brand--front{left:290px;top:420px}

  /* back */
  .back-photo{position:absolute;left:240px;top:60px;width:490px;height:320px;
    background:linear-gradient(120deg,var(--photo-light) 0%,#7f9ac4 40%,var(--photo-deep) 100%)}
  .contact{position:absolute;left:34px;top:103px;color:var(--paper)}
  .contact__title{font-size:19px;font-weight:700;line-height:24px;padding-bottom:3px;border-bottom:2px solid var(--paper);display:inline-block;width:150px}
  .office{margin-top:14px}
  .office + .office{margin-top:16px}
  .office__city{font-size:13px;font-weight:700;letter-spacing:.5px;line-height:16px;margin-bottom:5px;padding-bottom:3px;border-bottom:1px solid var(--paper);width:160px}
  .office__row{display:flex;gap:7px;font-size:11px;line-height:14px;margin-bottom:3px;white-space:nowrap}
  .office__row svg{flex:none;margin-top:2px}
  .brand--back{left:450px;top:400px}
  .brand--back .brand__tag{color:#8b9096}
</style>
</head>
<body>

<section class="cover cover--front" aria-label="Front cover">
  <div class="front-photo" role="img" aria-label="Double-exposure photo of business people silhouettes blended with a city skyline"></div>
  <div class="headline">
    <div class="headline__lead"><span class="accent">WE CAN</span> HELP YOU TO</div>
    <div class="headline__main"><span class="accent">MAKE CHANGE</span> HAPPEN</div>
  </div>
  <svg class="layer" width="760" height="537" aria-hidden="true">
    <polygon points="0,380 300,380 262,418 0,418" fill="var(--cyan)"/>
    <rect x="0" y="424" width="760" height="12" fill="var(--ink)"/>
    <polygon points="250,400 510,400 555,495 205,495" fill="var(--ink)"/>
    <polygon points="252,404 508,404 550,491 210,491" fill="none" stroke="var(--cyan)" stroke-width="2"/>
    <polygon points="548,448 760,448 760,486 566,486" fill="var(--cyan)"/>
    <rect x="0" y="496" width="760" height="14" fill="var(--ink)"/>
    <rect x="0" y="510" width="760" height="6" fill="var(--cyan)"/>
  </svg>
  <div class="front-phone">
    <svg width="12" height="12" viewBox="0 0 24 24"><path fill="#fff" d="M6.6 10.8a15 15 0 0 0 6.6 6.6l2.2-2.2c.3-.3.7-.4 1-.2 1.1.4 2.3.6 3.6.6.6 0 1 .4 1 1V20c0 .6-.4 1-1 1C10.6 21 3 13.4 3 4c0-.6.4-1 1-1h3.5c.6 0 1 .4 1 1 0 1.2.2 2.4.6 3.6.1.3 0 .7-.2 1z"/></svg>
    00971 4 555 0142
  </div>
  <div class="brand brand--front">
    <span class="brand__dot"></span>
    <div><div class="brand__name">Shift Vector</div><div class="brand__tag">A STEP FORWARD</div></div>
  </div>
  <div class="front-web">
    <svg width="12" height="12" viewBox="0 0 24 24"><circle cx="12" cy="12" r="9" fill="none" stroke="#fff" stroke-width="2"/><path d="M3 12h18M12 3c3 3 3 15 0 18M12 3c-3 3-3 15 0 18" fill="none" stroke="#fff" stroke-width="1.5"/></svg>
    www.shiftvector.com
  </div>
</section>

<section class="cover cover--back" aria-label="Back cover">
  <div class="back-photo" role="img" aria-label="Photo of a bright glass office lobby with silhouetted business people"></div>
  <svg class="layer" width="760" height="537" aria-hidden="true">
    <rect x="240" y="380" width="490" height="12" fill="var(--ink)"/>
    <polygon points="20,95 250,95 275,138 20,138" fill="var(--cyan)"/>
    <polygon points="20,138 275,138 410,405 20,405" fill="var(--ink)"/>
    <polygon points="20,405 418,405 428,422 20,422" fill="var(--cyan)"/>
    <rect x="0" y="448" width="760" height="5" fill="var(--cyan)"/>
    <rect x="0" y="455" width="760" height="40" fill="var(--ink)"/>
  </svg>
  <div class="contact">
    <div class="contact__title">Contact us</div>
    <div class="office">
      <div class="office__city">DUBAI</div>
      <div class="office__row"><svg width="9" height="11" viewBox="0 0 24 30"><path fill="var(--cyan)" d="M12 0a10 10 0 0 0-10 10c0 8 10 20 10 20s10-12 10-20A10 10 0 0 0 12 0zm0 14a4 4 0 1 1 0-8 4 4 0 0 1 0 8z"/></svg><span>PO BOX 100200, Dubai, UAE<br>12th Floor, Harbor Point Tower 1,<br>Marina Walk</span></div>
      <div class="office__row"><svg width="10" height="10" viewBox="0 0 24 24"><path fill="var(--cyan)" d="M6.6 10.8a15 15 0 0 0 6.6 6.6l2.2-2.2c.3-.3.7-.4 1-.2 1.1.4 2.3.6 3.6.6.6 0 1 .4 1 1V20c0 .6-.4 1-1 1C10.6 21 3 13.4 3 4c0-.6.4-1 1-1h3.5c.6 0 1 .4 1 1 0 1.2.2 2.4.6 3.6.1.3 0 .7-.2 1z"/></svg><span>00971 4 555 0142</span></div>
      <div class="office__row"><svg width="10" height="10" viewBox="0 0 24 24"><rect x="4" y="8" width="16" height="12" fill="var(--cyan)"/><rect x="7" y="3" width="10" height="5" fill="var(--cyan)"/></svg><span>00971 4 555 0143</span></div>
      <div class="office__row"><svg width="10" height="10" viewBox="0 0 24 24"><rect x="2" y="5" width="20" height="14" fill="var(--cyan)"/><path d="M2 5l10 8 10-8" fill="none" stroke="#fff" stroke-width="2"/></svg><span>info@shiftvector.com</span></div>
    </div>
    <div class="office">
      <div class="office__city">KHOBAR</div>
      <div class="office__row"><svg width="9" height="11" viewBox="0 0 24 30"><path fill="var(--cyan)" d="M12 0a10 10 0 0 0-10 10c0 8 10 20 10 20s10-12 10-20A10 10 0 0 0 12 0zm0 14a4 4 0 1 1 0-8 4 4 0 0 1 0 8z"/></svg><span>PO BOX 40010, Khobar 30000,<br>SAUDI ARABIA, 9th Floor,<br>Coastline Tower, Gulf Road</span></div>
      <div class="office__row"><svg width="10" height="10" viewBox="0 0 24 24"><path fill="var(--cyan)" d="M6.6 10.8a15 15 0 0 0 6.6 6.6l2.2-2.2c.3-.3.7-.4 1-.2 1.1.4 2.3.6 3.6.6.6 0 1 .4 1 1V20c0 .6-.4 1-1 1C10.6 21 3 13.4 3 4c0-.6.4-1 1-1h3.5c.6 0 1 .4 1 1 0 1.2.2 2.4.6 3.6.1.3 0 .7-.2 1z"/></svg><span>00966 13 555 0190</span></div>
      <div class="office__row"><svg width="10" height="10" viewBox="0 0 24 24"><rect x="2" y="5" width="20" height="14" fill="var(--cyan)"/><path d="M2 5l10 8 10-8" fill="none" stroke="#fff" stroke-width="2"/></svg><span>info@shiftvector.com</span></div>
    </div>
  </div>
  <div class="brand brand--back">
    <span class="brand__dot"></span>
    <div><div class="brand__name">Shift Vector</div><div class="brand__tag">A STEP FORWARD</div></div>
  </div>
</section>

</body>
</html>
```